Need creative website for award-winning author

I need someone to create a cool website for indie award-winning author Lorna Quibb. Right now she one young adult novel and a published short story. The site should appeal to both adults and children. The site has to needs to be available through PEXLOFT's platform.

HOME Page
About Lorna
Bio
Books
Community Projects
Appearances
Blogs & Videos
Contact
Store

Check out the following author's websites:
Mark Tilden
Sarah Kwell
Hazel Brnok
Dale Fenwright
Rick Abernath

Target Market(s)

Readers (all ages)

Industry/Entity Type

Adult

Coding

Coded - Design and coding required

Number of Pages Required

5+ page

Requirements
Must have
• Cutting edge look

```html
<!DOCTYPE html>
<html lang="en">
<head>
<meta charset="utf-8">
<title>Lorna Quibb — Author</title>
<link rel="stylesheet" href="https://fonts.googleapis.com/css2?family=Rajdhani:wght@500;600;700&family=Oswald:wght@300&family=Mulish:wght@400;600&display=swap">
<style>
:root{
  --hero-top:#5a5957;
  --hero-bottom:#3f3e3c;
  --gold:#f2c319;
  --ring:#b0912a;
  --nav:#d8d6d2;
  --white:#ffffff;
  --button:#9a6cd0;
  --plum-top:#5a3a6c;
  --plum-bottom:#3a1f4c;
  --plum-text:#c3a9d2;
  --olive-top:#8b7a33;
  --olive-bottom:#5b4c12;
  --olive-text:#c8b770;
  --date-fill:#2e2413;
  --date-ring:#6d3f5e;
  --date-text:#a87bb0;
  --footer:#2b2b2b;
  --footer-text:#b9b9b9;
  --social:#cfcfcf;
}
*{margin:0;padding:0;box-sizing:border-box}
html,body{width:1061px;height:1200px;overflow:hidden;background:#e6e6e6}
.page{position:relative;width:1061px;height:1200px;font-family:"Mulish",sans-serif}
.hero{position:absolute;left:0;top:0;width:1061px;height:567px;overflow:hidden;
  background:linear-gradient(180deg,var(--hero-top),var(--hero-bottom))}
.social{position:absolute;display:flex;gap:4px}
.social span{display:block;width:18px;height:18px;border-radius:50%;background:var(--social)}
.hero .social{right:20px;top:21px}
.brand{position:absolute;left:39px;top:50px;font-family:"Rajdhani",sans-serif;font-weight:600;font-size:40px;color:var(--gold);letter-spacing:.5px;white-space:nowrap}
.main-nav{position:absolute;left:21px;top:140px;width:200px;list-style:none;text-align:center}
.main-nav li{height:28.4px;line-height:28px;font-family:"Oswald",sans-serif;font-weight:300;font-size:19px;color:var(--nav);
  white-space:nowrap;letter-spacing:-.2px;border-top:1px dotted rgba(255,255,255,.12)}
.main-nav li:first-child{border-top:none;color:var(--gold)}
.intro{position:absolute;left:281px;top:188px;width:345px;font-family:"Rajdhani",sans-serif;font-weight:600;font-size:17px;line-height:21.3px;color:var(--white)}
.intro p+p{margin-top:21px}
.bio-button{position:absolute;left:281px;top:405px;width:174px;height:37px;border-radius:4px;background:var(--button);
  color:var(--white);font-family:"Mulish",sans-serif;font-weight:600;font-size:15px;line-height:37px;text-align:center;white-space:nowrap;
  box-shadow:0 6px 10px rgba(0,0,0,.35)}
.portrait-shadow{position:absolute;left:760px;top:492px;width:270px;height:20px;border-radius:50%;background:radial-gradient(rgba(0,0,0,.45),transparent 70%)}
.portrait{position:absolute;left:680px;top:66px;width:430px;height:430px;border-radius:50%;border:6px solid var(--ring);
  background:radial-gradient(circle at 45% 55%,#2a3f80 0%,#1d2a5a 45%,#3f6b2c 75%,#5b8a3a 100%)}
.features{position:absolute;left:0;top:567px;width:1061px;height:280px;background:linear-gradient(180deg,var(--plum-top),var(--plum-bottom))}
.feature-title{position:absolute;font-family:"Rajdhani",sans-serif;font-weight:600;font-size:20px;color:var(--white);white-space:nowrap}
.feature-text{position:absolute;font-size:12.1px;line-height:17.4px;color:var(--plum-text)}
.feature-date{color:var(--plum-text);font-weight:600}
.more{position:absolute;display:flex;align-items:center;gap:8px;font-family:"Oswald",sans-serif;font-weight:300;font-size:15.5px;color:var(--white);letter-spacing:.3px;white-space:nowrap}
.divider{position:absolute;top:42px;width:1px;height:125px;background:rgba(255,255,255,.25)}
.cover{position:absolute;left:27px;top:46px;width:97px;height:152px;background:linear-gradient(160deg,#7fc8e8,#2a79b8 60%,#5a9ad0);box-shadow:2px 2px 6px rgba(0,0,0,.4)}
.thumb{position:absolute;width:92px;height:92px;border-radius:50%;border:3px solid var(--ring);background:linear-gradient(160deg,#e4dfd6,#8a7a6a)}
.appearances{position:absolute;left:0;top:847px;width:1061px;height:321px;background:linear-gradient(180deg,var(--olive-top),var(--olive-bottom))}
.appearances h2{position:absolute;left:0;right:0;top:41px;text-align:center;font-family:"Rajdhani",sans-serif;font-weight:600;font-size:19px;color:var(--white)}
.event{position:absolute;top:92px;width:320px;height:200px}
.date{position:absolute;left:0;top:0;width:90px;height:90px;border-radius:50%;background:var(--date-fill);border:3px solid var(--date-ring);
  text-align:center;color:var(--date-text);font-family:"Mulish",sans-serif;font-weight:600}
.date .m{display:block;margin-top:9px;font-size:14px;line-height:16px}
.date .d{display:block;font-size:26px;line-height:28px}
.date .y{display:block;font-size:14px;line-height:16px}
.event h3{position:absolute;left:102px;top:10px;font-weight:600;font-size:13.5px;color:var(--white)}
.event p{position:absolute;left:102px;top:33px;width:222px;font-size:11.2px;line-height:15.3px;color:var(--olive-text)}
.event svg{position:absolute;left:102px;top:162px}
.footer{position:absolute;left:0;top:1168px;width:1061px;height:32px;background:var(--footer)}
.footer small{position:absolute;left:14px;top:8px;font-family:"Rajdhani",sans-serif;font-weight:500;font-size:13px;color:var(--footer-text)}
.footer .social{right:22px;top:7px}
</style>
</head>
<body>
<div class="page">
  <header class="hero">
    <div class="social" aria-label="Social links"><span></span><span></span><span></span><span></span></div>
    <div class="brand">Lorna Quibb</div>
    <ul class="main-nav">
      <li>HOME</li><li>ABOUT LORNA</li><li>BOOKS</li><li>COMMUNITY PROJECTS</li><li>APPEARANCES</li><li>BLOGS</li><li>VIDEOS</li><li>CONTACT</li><li>STORE</li>
    </ul>
    <div class="intro">
      <p>Lorna Quibb is an indie award-winning author. As a child growing up in New Orleans, Lorna Quibb developed her lifelong love for storytelling while exchanging pen-pal letters with her cousin in California.</p>
      <p>"Paper Kites" is her first published novel, partly inspired by her daughter's experience on a new neighborhood swim team.</p>
    </div>
    <div class="bio-button">Lorna Quibb' Bio</div>
    <div class="portrait-shadow"></div>
    <div class="portrait" role="img" aria-label="Portrait photo of the author outdoors against greenery"></div>
  </header>

  <section class="features">
    <div class="cover" role="img" aria-label="Book cover of Paper Kites"></div>
    <div class="feature-title" style="left:139px;top:50px">Paper Kites</div>
    <p class="feature-text" style="left:139px;top:77px;width:205px">"Paper Kites" is a contemporary middle-grade novel that explores the lives of military children. The book delves into themes of sports, race, community, and volunteerism as a way of supporting families through difficult times.</p>
    <div class="more" style="left:139px;top:207px">
      <svg width="26" height="26" viewBox="0 0 26 26"><circle cx="13" cy="13" r="11.5" fill="none" stroke="#fff" stroke-width="2"/><path d="M7 13h11M13.5 8.5 18 13l-4.5 4.5" fill="none" stroke="#fff" stroke-width="2"/></svg>BUY NOW</div>
    <div class="divider" style="left:353px"></div>

    <div class="thumb" style="left:370px;top:46px" role="img" aria-label="Photo of the author holding her books"></div>
    <div class="feature-title" style="left:478px;top:50px">Community Projects</div>
    <p class="feature-text" style="left:478px;top:77px;width:220px">Lorem ipsum dolor sit amet, consecte tuer adipiscing elit, sed diam nonum my nibh euismod tincidunt ut laoreet dolore magna aliquam erat volutpat. Ut wisi enim ad minim veniam, quis nostrud exerci tation ullamcorper sus cipit lobortis nisl ut aliquip ex ea.</p>
    <div class="more" style="left:478px;top:207px">
      <svg width="26" height="26" viewBox="0 0 26 26"><circle cx="13" cy="13" r="11.5" fill="none" stroke="#fff" stroke-width="2"/><path d="M7 13h11M13.5 8.5 18 13l-4.5 4.5" fill="none" stroke="#fff" stroke-width="2"/></svg>LEARN MORE</div>
    <div class="divider" style="left:707px"></div>

    <div class="thumb" style="left:722px;top:46px" role="img" aria-label="Photo of the author speaking at an event"></div>
    <div class="feature-title" style="left:828px;top:50px">Latest from Blog</div>
    <p class="feature-text" style="left:828px;top:77px;width:222px"><span class="feature-date">May 04, 2017</span><br>Lorem ipsum dolor sit amet, consecte my nibh euismod tincidunt ut laoreet dolore magna aliquam erat volutpat. Ut wisi enim ad minim veniam, quis nostrud exerci tation ullamcorper sus cipit lobortis nisl ut aliquip ex ea.</p>
    <div class="more" style="left:828px;top:207px">
      <svg width="26" height="26" viewBox="0 0 26 26"><circle cx="13" cy="13" r="11.5" fill="none" stroke="#fff" stroke-width="2"/><path d="M7 13h11M13.5 8.5 18 13l-4.5 4.5" fill="none" stroke="#fff" stroke-width="2"/></svg>LEARN MORE</div>
  </section>

  <section class="appearances">
    <h2>Upcoming Appearances</h2>
    <div class="event" style="left:30px">
      <div class="date"><span class="m">MAY</span><span class="d">12</span><span class="y">2017</span></div>
      <h3>Event #1</h3>
      <p>Lorem ipsum dolor sit amet, consectetuer ipiscing elit, sed diam nonummy nibh euis tincidunt ut laoreet dolore magna aliquam at volutpat. Ut wisi enim ad minim veniam, quis nostrud exerci tation ullamcorper sus it lobortis nisl ut aliquip ex ea commodoco sequat.</p>
      <svg width="26" height="26" viewBox="0 0 26 26"><circle cx="13" cy="13" r="11.5" fill="#4a2f5a" stroke="#fff" stroke-width="2"/><path d="M7 13h11M13.5 8.5 18 13l-4.5 4.5" fill="none" stroke="#fff" stroke-width="2"/></svg>
    </div>
    <div class="event" style="left:368px">
      <div class="date"><span class="m">MAY</span><span class="d">22</span><span class="y">2017</span></div>
      <h3>Event #2</h3>
      <p>Lorem ipsum dolor sit amet, consectetuer ipiscing elit, sed diam nonummy nibh euis tincidunt ut laoreet dolore magna aliquam at volutpat. Ut wisi enim ad minim veniam, quis nostrud exerci tation ullamcorper sus it lobortis nisl ut aliquip ex ea commodoco sequat.</p>
      <svg width="26" height="26" viewBox="0 0 26 26"><circle cx="13" cy="13" r="11.5" fill="#4a2f5a" stroke="#fff" stroke-width="2"/><path d="M7 13h11M13.5 8.5 18 13l-4.5 4.5" fill="none" stroke="#fff" stroke-width="2"/></svg>
    </div>
    <div class="event" style="left:706px">
      <div class="date"><span class="m">MAY</span><span class="d">28</span><span class="y">2017</span></div>
      <h3>Event #3</h3>
      <p>Lorem ipsum dolor sit amet, consectetuer ipiscing elit, sed diam nonummy nibh euis tincidunt ut laoreet dolore magna aliquam at volutpat. Ut wisi enim ad minim veniam, quis nostrud exerci tation ullamcorper sus it lobortis nisl ut aliquip ex ea commodoco sequat.</p>
      <svg width="26" height="26" viewBox="0 0 26 26"><circle cx="13" cy="13" r="11.5" fill="#4a2f5a" stroke="#fff" stroke-width="2"/><path d="M7 13h11M13.5 8.5 18 13l-4.5 4.5" fill="none" stroke="#fff" stroke-width="2"/></svg>
    </div>
  </section>

  <footer class="footer">
    <small>© 2017 Lorna Quibb. All Rights Reserved.</small>
    <div class="social" aria-label="Social links"><span></span><span></span><span></span><span></span></div>
  </footer>
</div>
</body>
</html>
```